Quorvin Upcoming Gigs

One page graphic with my upcoming dates. Logo and photo attached, and sample from last flyer. Text:

QUORVIN

UPCOMING DATES

3/26/18 Tidal Plums (Las Vegas, NV)

4/1/18 Venture Hollow 2847 M St (Sac, CA)

4/8/18 Amber Heron (Sac, CA)

5/5/18 Low Ceiling @ Silver Moth (Sac, CA)

5/10/18 Pellman Art Museum (Sac, CA)

5/11/18 Vif Brume @ Cafe du Lierre (Sac, CA)

5/27/18 Sonnlicht JTR @ Vox (Sac, CA)

Save The Date: 9/21/18 Lanterns Festival (Puerto Nuevo, MX)

plazabook.example/quorvin482

Target Market(s)

House/Electronic Music

Industry/Entity Type

Night Club

Font styles to use
Sans Serif

Colors

Designer to choose colors to be used in the design.

Requirements
Must have
• Quorvin logo or something that looks good instead. Prefer photo to be in but not necessary.
Nice to have

```html
<!DOCTYPE html>
<html lang="en">
<head>
<meta charset="utf-8">
<title>Quorvin Upcoming Dates</title>
<link rel="stylesheet" href="https://fonts.googleapis.com/css2?family=Lato:wght@400;700&family=Oswald:wght@300;500;600;700&display=swap">
<style>
  :root {
    --page-bg: #d6d6d6;
    --ink: #050507;
    --logo-panel: #0c0c10;
    --brand-blue: #1739a8;
    --brand-yellow: #fcc93a;
    --paper: #ffffff;
    --photo-deep: #140a2e;
    --photo-violet: #4a2bb0;
    --photo-magenta: #b0306e;
  }
  * { box-sizing: border-box; margin: 0; padding: 0; }
  html, body {
    width: 1200px; height: 1200px; overflow: hidden;
    background: var(--page-bg);
  }
  .banner {
    position: absolute; left: 20px; top: 297px;
    width: 1278px; height: 667px;
    transform: scale(0.9077); transform-origin: top left;
    background: var(--ink); overflow: hidden;
    font-family: "Lato", sans-serif;
  }
  .dj-photo {
    position: absolute; left: 668px; top: 0; width: 610px; height: 667px;
    background:
      radial-gradient(ellipse 45% 35% at 35% 20%, rgba(140,70,220,.55), transparent 70%),
      radial-gradient(ellipse 30% 30% at 55% 50%, rgba(230,110,170,.55), transparent 70%),
      radial-gradient(ellipse 60% 25% at 55% 80%, rgba(176,48,110,.55), transparent 70%),
      linear-gradient(160deg, var(--photo-violet) 0%, var(--photo-deep) 60%, #0a0612 100%);
  }
  .dj-photo::after {
    content: ""; position: absolute; inset: 0;
    background: linear-gradient(90deg, var(--ink) 0%, rgba(5,5,7,0) 18%);
  }
  .logo-panel {
    position: absolute; left: 20px; top: 15px; width: 412px; height: 95px;
    background: var(--logo-panel);
  }
  .logo-name {
    position: absolute; left: 16px; top: 8px;
    font-family: "Oswald", sans-serif; font-weight: 700; font-size: 80px;
    line-height: 1; letter-spacing: 3px; color: var(--brand-blue);
  }
  .heading {
    position: absolute; left: 42px; top: 122px;
    display: flex; align-items: center; gap: 14px;
    font-family: "Oswald", sans-serif;
  }
  .heading-main { font-weight: 600; font-size: 60px; color: var(--brand-yellow); line-height: 1; }
  .heading-box {
    border: 2px solid var(--paper); color: var(--paper);
    font-weight: 300; font-size: 42px; line-height: 1; padding: 2px 12px 3px;
  }
  .gig {
    position: absolute; left: 35px; width: 590px; height: 34px;
  }
  .gig svg { position: absolute; inset: 0; }
  .gig span { position: absolute; top: 0; line-height: 34px; white-space: nowrap; }
  .gig-date { left: 24px; color: var(--paper); font-weight: 700; font-size: 19px; }
  .gig-venue { left: 150px; color: var(--ink); font-size: 17px; font-weight: 400; }
  .gig-place { left: 409px; color: var(--ink); font-weight: 700; font-size: 18px; }
  .save-date {
    position: absolute; left: 42px; top: 574px;
    font-family: "Oswald", sans-serif; font-weight: 500; font-size: 28px; color: var(--paper);
  }
  .save-rule { position: absolute; left: 45px; top: 615px; width: 69px; height: 4px; background: var(--brand-yellow); }
  .feature {
    position: absolute; left: 239px; top: 578px; font-size: 28px; color: var(--paper);
  }
  .feature-date { color: var(--brand-yellow); font-weight: 700; margin-right: 8px; }
  .feature-place { position: absolute; left: 240px; top: 620px; font-size: 17px; color: var(--paper); }
  .social {
    position: absolute; right: 28px; top: 618px;
    display: flex; align-items: center; gap: 10px;
    font-size: 20px; letter-spacing: 2px; color: var(--paper);
  }
  .social-mark { width: 12px; height: 12px; background: var(--brand-yellow); }
</style>
</head>
<body>
<div class="banner">
  <div class="dj-photo" role="img" aria-label="Photo of the DJ in a cap working the decks under purple and pink club lights against a brick wall"></div>

  <div class="logo-panel"><div class="logo-name">QUORVIN</div></div>

  <div class="heading">
    <span class="heading-main">UPCOMING</span>
    <span class="heading-box">DATES</span>
  </div>

  <svg width="0" height="0" style="position:absolute">
    <defs>
      <g id="gig-shape">
        <polygon points="383,0 537,0 549,17 537,34 383,34 395,17" fill="var(--brand-yellow)"/>
        <polygon points="6,0 114,0 126,17 114,34 0,34" fill="var(--brand-blue)"/>
        <polygon points="122,0 374,0 387,17 374,34 122,34 134,17" fill="var(--paper)"/>
        <polyline points="129,3 371,3 383,17 371,31 129,31 140,17 129,3" fill="none" stroke="var(--ink)" stroke-width="2"/>
      </g>
    </defs>
  </svg>

  <div class="gig" style="top:202px"><svg viewBox="0 0 590 34"><use href="#gig-shape"/></svg><span class="gig-date">3/26/18</span><span class="gig-venue">Tidal Plums</span><span class="gig-place">Las Vegas, NV</span></div>
  <div class="gig" style="top:257px"><svg viewBox="0 0 590 34"><use href="#gig-shape"/></svg><span class="gig-date">4/1/18</span><span class="gig-venue">Venture Hollow 2847 M St</span><span class="gig-place">Sac, CA</span></div>
  <div class="gig" style="top:311px"><svg viewBox="0 0 590 34"><use href="#gig-shape"/></svg><span class="gig-date">4/8/18</span><span class="gig-venue">Amber Heron</span><span class="gig-place">Sac, CA</span></div>
  <div class="gig" style="top:362px"><svg viewBox="0 0 590 34"><use href="#gig-shape"/></svg><span class="gig-date">5/5/18</span><span class="gig-venue">Low Ceiling @ Silver Moth</span><span class="gig-place">Sac, CA</span></div>
  <div class="gig" style="top:414px"><svg viewBox="0 0 590 34"><use href="#gig-shape"/></svg><span class="gig-date">5/10/18</span><span class="gig-venue">Pellman Art Museum</span><span class="gig-place">Sac, CA</span></div>
  <div class="gig" style="top:466px"><svg viewBox="0 0 590 34"><use href="#gig-shape"/></svg><span class="gig-date">5/11/18</span><span class="gig-venue">Vif Brume @ Cafe du Lierre</span><span class="gig-place">Sac, CA</span></div>
  <div class="gig" style="top:523px"><svg viewBox="0 0 590 34"><use href="#gig-shape"/></svg><span class="gig-date">5/27/18</span><span class="gig-venue">Sonnlicht JTR @ Vox</span><span class="gig-place">Sac, CA</span></div>

  <div class="save-date">Save The Date:</div>
  <div class="save-rule"></div>
  <div class="feature"><span class="feature-date">9/21/18</span>Lanterns Festival</div>
  <div class="feature-place">(Puerto Nuevo, MX)</div>

  <div class="social"><span class="social-mark"></span><span>plazabook.example/quorvin482</span></div>
</div>
</body>
</html>
```